Business Card & Letterhead Design

We a financial advice company based in Australia. We provide advice to wealthy farmers.

We are changing our business name FROM Brightmere Financial TO Calderstone Wealth and we need a new letterhead and double sided business card design

Attached is designs from our previous branding (Brightmere Financial) as it includes all the details we require on the new Calderstone Wealth business cards and letterhead.

```html
<!DOCTYPE html>
<html lang="en">
<head>
<meta charset="utf-8">
<title>Calderstone Wealth Stationery</title>
<link href="https://fonts.googleapis.com/css2?family=Montserrat:ital,wght@0,400;0,500;0,600;1,400&display=swap" rel="stylesheet">
<style>
  :root{
    --bg:#a9a9a9;
    --paper:#ffffff;
    --ink:#3d3d3d;
    --ink-soft:#6b6b6b;
    --band:#474747;
    --rule:#8a8a8a;
  }
  *{margin:0;padding:0;box-sizing:border-box}
  html,body{width:1200px;height:900px;overflow:hidden}
  body{background:var(--bg);font-family:'Montserrat',sans-serif;color:var(--ink);position:relative}

  .letterhead{position:absolute;left:150px;top:90px;width:520px;height:720px;background:var(--paper);box-shadow:0 4px 14px rgba(0,0,0,.25)}
  .brand{position:absolute;text-align:center}
  .brand-dot{display:block;margin:0 auto 6px;border:1.5px solid var(--ink);border-radius:50%}
  .brand-name{font-weight:500;letter-spacing:.06em;text-transform:uppercase;white-space:nowrap}
  .brand-tag{font-weight:400;letter-spacing:.32em;text-transform:uppercase;color:var(--ink-soft);white-space:nowrap}
  .letterhead .brand{left:42px;top:34px;width:190px}
  .letterhead .brand-dot{width:38px;height:38px}
  .letterhead .brand-name{font-size:14px}
  .letterhead .brand-tag{font-size:6px;margin-top:2px}

  .contacts{list-style:none}
  .contacts li{display:flex;align-items:center;gap:5px;white-space:nowrap}
  .contacts svg{flex:none}
  .letterhead .contacts{position:absolute;left:296px;top:38px;font-size:8.5px;line-height:15px}

  .legal{position:absolute;left:0;right:0;text-align:center;font-size:7.8px;line-height:11px;color:var(--ink-soft)}
  .legal-top{top:594px}
  .legal-rule{position:absolute;left:48px;right:48px;top:622px;border-top:1px solid var(--rule)}
  .legal-bottom{top:628px}
  .footer-band{position:absolute;left:0;bottom:0;width:520px;height:36px}
  .motto{position:absolute;left:0;right:0;bottom:9px;text-align:center;font-style:italic;font-size:9.5px;color:#fff}

  .card{position:absolute;left:770px;width:340px;height:207px;box-shadow:0 4px 12px rgba(0,0,0,.25)}
  .card-back{top:255px;background:var(--band);color:#fff;text-align:center}
  .card-back .brand{left:0;right:0;top:22px}
  .card-back .brand-dot{width:34px;height:34px;border-color:#fff}
  .card-back .brand-name{font-size:12px;color:#fff}
  .services{position:absolute;left:0;right:0;top:104px;font-size:8.5px;line-height:14px;font-weight:500}
  .licensee{position:absolute;left:0;right:0;top:150px;font-size:6.8px;line-height:13px;color:#ddd}

  .card-front{top:500px;background:var(--paper)}
  .card-front .brand{left:14px;top:16px;width:130px}
  .card-front .brand-dot{width:24px;height:24px;margin-bottom:4px}
  .card-front .brand-name{font-size:9.5px}
  .card-front .brand-tag{font-size:4.2px}
  .person{position:absolute;right:16px;top:18px;text-align:right;font-size:6.5px;line-height:9px;color:var(--ink-soft)}
  .person-name{font-size:9px;font-weight:600;color:var(--ink);text-transform:uppercase}
  .person-name small{font-size:4.5px;font-weight:400;text-transform:none;color:var(--ink-soft)}
  .card-rule{position:absolute;left:14px;right:16px;top:72px;border-top:1px solid var(--rule)}
  .card-front .contacts{position:absolute;left:14px;top:80px;font-size:6px;line-height:10.5px}
  .address{position:absolute;right:16px;top:80px;text-align:right;font-size:5.8px;line-height:10px;color:var(--ink-soft)}
  .address strong{font-weight:600;color:var(--ink);text-transform:uppercase}
  .card-band{position:absolute;left:0;bottom:0;width:340px;height:20px}
  .card-motto{position:absolute;left:0;right:0;bottom:4px;text-align:center;font-style:italic;font-size:6px;color:#fff}
</style>
</head>
<body>

<svg width="0" height="0" style="position:absolute">
  <defs>
    <symbol id="ico-phone" viewBox="0 0 12 12"><circle cx="6" cy="6" r="5.3" fill="none" stroke="currentColor" stroke-width="1"/><path d="M4 3.5c-.5.6-.4 1.7.6 2.9s2.3 1.8 2.9 1.4l.6-.6-1-1-.6.4c-.5-.2-1-.8-1.3-1.3l.4-.6-1-1z" fill="currentColor"/></symbol>
    <symbol id="ico-mobile" viewBox="0 0 12 12"><circle cx="6" cy="6" r="5.3" fill="none" stroke="currentColor" stroke-width="1"/><rect x="4.4" y="3" width="3.2" height="6" rx=".6" fill="none" stroke="currentColor" stroke-width=".8"/></symbol>
    <symbol id="ico-mail" viewBox="0 0 12 12"><circle cx="6" cy="6" r="5.3" fill="none" stroke="currentColor" stroke-width="1"/><rect x="3.5" y="4.2" width="5" height="3.6" fill="none" stroke="currentColor" stroke-width=".8"/><path d="M3.5 4.2 6 6.2 8.5 4.2" fill="none" stroke="currentColor" stroke-width=".8"/></symbol>
    <symbol id="ico-web" viewBox="0 0 12 12"><circle cx="6" cy="6" r="5.3" fill="none" stroke="currentColor" stroke-width="1"/><circle cx="6" cy="6" r="2.6" fill="none" stroke="currentColor" stroke-width=".8"/><path d="M3.4 6h5.2M6 3.4v5.2" stroke="currentColor" stroke-width=".6"/></symbol>
  </defs>
</svg>

<section class="letterhead">
  <div class="brand">
    <span class="brand-dot"></span>
    <div class="brand-name">Calderstone Wealth</div>
    <div class="brand-tag">Strategic Financial Advice</div>
  </div>

  <ul class="contacts">
    <li><svg width="10" height="10"><use href="#ico-phone"/></svg>(07) 3000 1842</li>
    <li><svg width="10" height="10"><use href="#ico-phone"/></svg>(07) 3000 5219</li>
    <li><svg width="10" height="10"><use href="#ico-mobile"/></svg>0400 628 317</li>
    <li><svg width="10" height="10"><use href="#ico-mail"/></svg>sam@calderstonewealth.com.au</li>
    <li><svg width="10" height="10"><use href="#ico-web"/></svg>www.calderstonewealth.com.au</li>
  </ul>

  <p class="legal legal-top">Harwick Holdings Pty Ltd - ATF The Marrow Creek Trust - Calderstone Wealth<br>ABN: 12 345 678 901 - Corporate Authorised - Representative of Keystone Advisory Services Limited</p>
  <div class="legal-rule"></div>
  <p class="legal legal-bottom">Keystone Advisory Services Limited - ABN: 98 765 432 109<br>Australian Financial Services Licence - Licence Number: 100 200<br>Principle Address: 120 Harbour Rd. P.O. Box 4410 Melbourne VIC 3000</p>

  <svg class="footer-band" viewBox="0 0 520 36" aria-hidden="true">
    <polygon points="0,8 172,8 180,24 188,8 372,8 380,24 388,8 520,8 520,36 0,36" fill="var(--band)"/>
    <polygon points="180,24 188,8 372,8 380,24 380,36 180,36" fill="var(--band)"/>
  </svg>
  <p class="motto">A Referral Built Business</p>
</section>

<section class="card card-back">
  <div class="brand">
    <span class="brand-dot"></span>
    <div class="brand-name">Calderstone Wealth</div>
  </div>
  <p class="services">Life &amp; TPD Insurance | Income Protection<br>Financial Planning | Retirement Planning</p>
  <p class="licensee">Keystone Advisory Services Limited<br>Australian Financial Services Licensee License Number: 100200</p>
</section>

<section class="card card-front">
  <div class="brand">
    <span class="brand-dot"></span>
    <div class="brand-name">Calderstone Wealth</div>
    <div class="brand-tag">Strategic Financial Advice</div>
  </div>
  <div class="person">
    <div class="person-name">Sam Reid <small>B.Com Dip.FP CFP</small></div>
    Managing Director<br>Authorised Representative
  </div>
  <div class="card-rule"></div>
  <ul class="contacts">
    <li><svg width="7" height="7"><use href="#ico-phone"/></svg>(07) 3000 1842</li>
    <li><svg width="7" height="7"><use href="#ico-phone"/></svg>(07) 3000 5219</li>
    <li><svg width="7" height="7"><use href="#ico-mobile"/></svg>0400 628 317</li>
    <li><svg width="7" height="7"><use href="#ico-mail"/></svg>sam@calderstonewealth.com.au</li>
    <li><svg width="7" height="7"><use href="#ico-web"/></svg>www.calderstonewealth.com.au</li>
  </ul>
  <p class="address"><strong>Calderstone Wealth</strong><br>Suite 14, 8 Ridgeway St,<br>Riverbend, QLD 4100<br>P.O. Box 5120<br>Riverbend, QLD 4100</p>
  <svg class="card-band" viewBox="0 0 340 20" aria-hidden="true">
    <polygon points="0,6 112,6 117,16 122,6 218,6 223,16 228,6 340,6 340,20 0,20" fill="var(--band)"/>
    <polygon points="117,16 122,6 218,6 223,16 223,20 117,20" fill="var(--band)"/>
  </svg>
  <p class="card-motto">A Referral Built Business</p>
</section>

</body>
</html>
```